Business Card Design Project

We consult with hotels on setting rates and maximizing a revenue strategy

Industry/Entity Type

Business

Contact Information for Business Card

I am not sure what I want. Our company offers high level consulting to hotels around the country but we are also laid back. I would like something that is professional but also shows the laid back side

```html
<!DOCTYPE html>
<html lang="en">
<head>
<meta charset="utf-8">
<title>Keelwater Revenue Management Solutions – Business Cards</title>
<link rel="stylesheet" href="https://fonts.googleapis.com/css2?family=Lato:wght@400;700&display=swap">
<style>
  :root {
    --bg: #e4e6e6;
    --teal: #5f9e9b;
    --teal-light: #c6dedd;
    --teal-mid: #86b8b5;
    --brown: #2f211d;
    --ink: #222;
    --white: #ffffff;
  }
  * { margin: 0; padding: 0; box-sizing: border-box; }
  html, body { width: 1200px; height: 898px; overflow: hidden; background: var(--bg); }
  body { position: relative; font-family: "Lato", sans-serif; }

  .card {
    position: absolute;
    left: 290px;
    width: 620px;
    height: 354px;
    overflow: hidden;
    box-shadow: 0 6px 18px rgba(0,0,0,0.18);
  }
  .card-front {
    top: 60px;
    background: radial-gradient(ellipse at 52% 38%, var(--teal-light) 0%, var(--teal-mid) 55%, var(--teal) 100%);
  }
  .card-back { top: 480px; background: var(--white); }

  .front-url {
    position: absolute; top: 34px; right: 40px;
    color: var(--white); font-size: 19px; letter-spacing: 1.5px;
  }
  .front-brand {
    position: absolute; right: 40px; bottom: 110px;
    color: var(--brown); font-weight: 700; font-size: 64px; letter-spacing: 2px;
    text-transform: uppercase; line-height: 1;
  }
  .front-tagline {
    position: absolute; right: 40px; bottom: 62px;
    background: var(--brown); color: var(--white);
    font-weight: 700; font-size: 21px; padding: 6px 16px;
  }

  .back-swoosh { position: absolute; top: 0; right: 0; }

  .back-brand {
    position: absolute; left: 48px; top: 96px;
    display: flex; align-items: center; gap: 12px;
  }
  .brand-mark { width: 22px; height: 22px; background: var(--teal); }
  .brand-name {
    color: var(--brown); font-weight: 700; font-size: 34px;
    letter-spacing: 1.5px; text-transform: uppercase;
  }
  .back-tagline {
    position: absolute; left: 48px; top: 142px;
    color: var(--brown); font-size: 15px; font-weight: 700;
  }

  .contact-list {
    position: absolute; left: 48px; bottom: 34px; list-style: none;
    color: var(--ink); font-size: 18px; line-height: 27px;
  }
  .contact-list li { display: flex; align-items: center; gap: 14px; }
  .contact-list svg { width: 16px; height: 16px; fill: var(--teal); }

  .person {
    position: absolute; right: 48px; bottom: 86px; text-align: right;
  }
  .person-name { color: var(--ink); font-size: 26px; }
  .person-title { color: var(--teal); font-size: 18px; margin-top: 2px; }
</style>
</head>
<body>

<section class="card card-front" aria-label="Card front">
  <p class="front-url">www.KeelwaterRMS.com</p>
  <p class="front-brand">Keelwater</p>
  <p class="front-tagline">Revenue Management Solutions</p>
</section>

<section class="card card-back" aria-label="Card back">
  <svg class="back-swoosh" width="620" height="260" viewBox="0 0 620 260" aria-hidden="true">
    <defs>
      <linearGradient id="swoosh-teal" x1="0" y1="0" x2="1" y2="0">
        <stop offset="0" stop-color="#c9e0df"/>
        <stop offset="1" stop-color="#5f9e9b"/>
      </linearGradient>
    </defs>
    <path d="M280 0 L620 0 L620 150 C560 70 440 18 280 0 Z" fill="#2f211d"/>
    <path d="M300 10 C450 28 560 86 620 190 L620 228 C545 110 440 48 300 10 Z" fill="url(#swoosh-teal)"/>
    <path d="M520 40 C570 70 600 100 620 130 L620 150 C600 115 565 80 520 40 Z" fill="#ffffff" opacity="0.6"/>
  </svg>

  <div class="back-brand">
    <span class="brand-mark"></span>
    <span class="brand-name">Keelwater</span>
  </div>
  <p class="back-tagline">Revenue Management Solutions</p>

  <div class="person">
    <p class="person-name">Dana Whitlock</p>
    <p class="person-title">Regional Revenue Manager</p>
  </div>

  <ul class="contact-list">
    <li>
      <svg viewBox="0 0 16 16" aria-label="Phone"><path d="M3 1 L6 1 L7 5 L5 6 C6 8 8 10 10 11 L11 9 L15 10 L15 13 C15 14 14 15 13 15 C6 15 1 10 1 3 C1 2 2 1 3 1 Z"/></svg>
      503-555-0148
    </li>
    <li>
      <svg viewBox="0 0 16 16" aria-label="Fax"><rect x="4" y="1" width="8" height="4"/><rect x="1" y="6" width="14" height="6" rx="1"/><rect x="4" y="10" width="8" height="5"/></svg>
      503-555-0172
    </li>
    <li>
      <svg viewBox="0 0 16 16" aria-label="Email"><path d="M1 3 H15 V13 H1 Z M1 3 L8 9 L15 3" stroke="#fff" stroke-width="1"/></svg>
      Dana@KeelwaterRMS.com
    </li>
    <li>
      <svg viewBox="0 0 16 16" aria-label="Website"><circle cx="8" cy="8" r="7"/><path d="M1 8 H15 M8 1 C5 5 5 11 8 15 M8 1 C11 5 11 11 8 15" stroke="#fff" stroke-width="1" fill="none"/></svg>
      www.KeelwaterRMS.com
    </li>
  </ul>
</section>

</body>
</html>
```